Website design for Cambridge based systematic hedge fund

We have run previous craftmosaic competitions to design our company logo, business cards and the styling of our presentation deck (see attached files).
As the final step we are looking to get a website designed that is thematically consistent with these existing elements of our branding.
You can find some of our competitors websites below:
https://www.quelmarsh.example/
https://www.fenloor.example/
https://www.pyvart.example/
https://www.dulvet.example/
https://www.orbelmfunds.example/
https://www.valtrigo.example/
https://www.meskilfunds.example/home
We would like to have a website that works well on both mobile devices and desktops. Either just as one page that can be scrolled down, with links at the top that skips to certain sections, or a few separate pages that can be navigated by a top menu.
It should look professional, we are not after lots of animations or unnecessary transitions, and in particular the website must be smooth to navigate. We would like to avoid having peoples of people, we are happy to make use of elements from the presentation (for example the style of the cover slide, or the section slides with the faded bridge in the background), or 'financial' style images.
We would like to have the following sections for now. For some of these some example text has been provided, final text may change but it will be of similar length. For the other sections we are happy to just have template text for now. At the moment we are mainly interested to see styles/layouts as words can be added easily afterwards:
1) We will need a disclaimer pop up the first time someone visits the site (see for example the meskilfunds example).
2) Top page - company name, then in larger text "Bringing AI and Statistical Inference to Financial Markets", and somewhere in smaller text "Harlow Vectors is a quantitative asset manager with the singular focus of delivering algorithmic strategies that work"
3) "About us" section: will describe us as a company, details our approach, company values, and explains the company logo.
Example text:
"We deliver consistent alpha across liquid markets through the application of proprietary IP in Bayesian inference, machine learning and artificial intelligence. We are a multi-disciplinary team founded by experienced finance professionals from premier institutions, leading academics from the Thornbury Stellar Unit at Ashmere College and world-class software engineers.
Our logo portrays a sillhoute of the lattice walkway at Ashmere College. Our unique scientific approach allows us to bridge cutting-edge mathematical research and computing expertise with financial knowledge to bring algorithmns that work to liquid markets"
4) Hiring section, detailing our culture, what we are looking for.
Example text:
"We are always looking for exceptional talent to join our entrepreneurial team. We are looking for individuals who are creative thinkers, can demonstrate analytical rigour and are passionate about the intersection of science, finance and technology.
We prioritise having a company culture that promotes sharing ideas in a safe, collaborative research environment. We make sure that every member of the team has the oppertunity to explore their own ideas through weekly 'innovation time', and ensure that everyone gets the support they need to continue to grow as individuals within the company."
5) A section for news/press releases
6) Contact us area at the bottom with office location and email. We will need to list 3 addresses for our Cambridge, London and Singapore offices, along with a couple of contact emails or phone numbers
7) A client login button at the top that will take them to a different website (unrelated to this one).

```html
<!DOCTYPE html>
<html lang="en">
<head>
<meta charset="utf-8">
<title>Harlow Vectors</title>
<link rel="stylesheet" href="https://fonts.googleapis.com/css2?family=Roboto:wght@300;400;500;700&display=swap">
<style>
:root{
  --navy:#0b3d6e;
  --coral:#f25c54;
  --ink:#3c3c3c;
  --heading:#3d4a5c;
  --muted:#9a9a9a;
  --pale:#f7f7f8;
  --line:#e6e6e8;
  --tab-idle:#e1e1e4;
  --white:#ffffff;
}
*{margin:0;padding:0;box-sizing:border-box}
html,body{width:1200px;height:3604px;overflow:hidden}
body{font-family:'Roboto',Arial,sans-serif;background:var(--white);position:relative;color:var(--ink)}
.abs{position:absolute}
.nowrap{white-space:nowrap}
.jl{display:block;text-align:justify;text-align-last:justify}

/* hero */
.hero-photo{left:0;top:0;width:1200px;height:600px;background:linear-gradient(160deg,#1c2634 0%,#34414f 35%,#1a2330 55%,#6b4a25 72%,#20262f 90%)}
.brand{left:74px;top:28px;color:var(--white);font-size:13px;font-weight:700;letter-spacing:.5px;display:flex;align-items:center;gap:7px}
.brand-dot{width:10px;height:10px;border-radius:50%;background:var(--white)}
.nav{top:29px;left:0;width:1200px;height:20px}
.nav a{position:absolute;color:var(--white);text-decoration:none;font-size:13px;top:0}
.login{left:1038px;top:22px;width:86px;height:31px;background:var(--navy);color:var(--white);font-size:13px;display:flex;align-items:center;justify-content:center}
.band{left:0;top:376px;width:849px;height:224px;background:var(--navy)}
.band-rule{top:376px;width:1px;height:224px;background:rgba(255,255,255,.35)}
.band-kicker{left:152px;top:414px;font-size:9px;color:rgba(255,255,255,.7)}
.band-title{left:152px;top:442px;font-size:15px;line-height:23.5px;font-weight:500;color:var(--white)}
.band-copy{left:511px;top:429px;font-size:12.5px;line-height:26.3px;color:var(--white)}
.scroll-box{left:849px;top:376px;width:275px;height:224px;background:var(--white);display:flex;align-items:center;justify-content:center;font-size:12.5px;font-weight:500;color:var(--navy)}
.scroll-arrow{left:1149px;top:472px}

/* about */
.about{left:0;top:600px;width:1200px;height:600px;background-color:var(--pale);
  background-image:linear-gradient(var(--line) 1px,transparent 1px),linear-gradient(90deg,var(--line) 1px,transparent 1px);background-size:28px 28px}
.about-side{left:74px;top:727px;width:88px;height:351px;background:var(--white)}
.about-label{left:74px;top:767px;width:88px;height:150px;display:flex;align-items:center;justify-content:center}
.about-label span{transform:rotate(-90deg);font-size:32px;font-weight:700;color:#e4e4e6;white-space:nowrap}
.about-photo{left:162px;top:727px;width:525px;height:351px;background:linear-gradient(135deg,#d9dde2 0%,#b8c0c8 40%,#5c6670 75%,#2c333b 100%)}
.about-card{left:494px;top:761px;width:630px;height:285px;background:var(--white);padding:30px 33px}
.about-card h3{font-size:23px;font-weight:400;line-height:38px;color:var(--heading)}
.about-card p{margin-top:18px;font-size:12.5px;line-height:26.5px;color:var(--muted);white-space:nowrap}
.circle-btn{display:block;margin-top:16px;width:28px;height:28px}

/* approach */
.section-title{font-size:42px;font-weight:700;color:var(--ink);letter-spacing:.3px}
.approach-title{left:74px;top:1258px}
.tabs{left:74px;top:1352px;width:1050px;height:55px}
.tab{position:absolute;top:0;height:55px;width:350px;font-size:17px;font-weight:700;padding:21px 0 0 20px;border-bottom:2px solid #eeeef0;color:var(--tab-idle)}
.tab b{margin-right:10px}
.tab.active{color:var(--navy);border-bottom:3px solid var(--navy)}
.tab-div{position:absolute;top:0;width:2px;height:55px;background:#eeeef0}
.approach-copy{left:74px;top:1466px;width:524px;font-size:12px;line-height:26.4px;color:var(--muted)}
.approach-copy p+p{margin-top:18px}
.approach-photo{left:710px;top:1459px;width:414px;height:274px;background:linear-gradient(120deg,#a58460 0%,#e9e6df 40%,#c9ccd1 65%,#5a6f8b 100%)}
.badge{left:700px;top:1683px;width:133px;height:61px;background:var(--navy);display:flex;align-items:center;gap:10px;padding-left:12px;color:var(--white);font-size:10px;line-height:18px}

/* values */
.values{left:0;top:1801px;width:1200px;height:600px;background:var(--navy);overflow:hidden}
.values-box{left:136px;top:1801px;width:307px;height:308px;background:var(--coral);padding:100px 0 0 73px;color:var(--white);font-size:42px;font-weight:700;line-height:60px}
.values-lede{left:226px;top:2186px;font-size:18px;line-height:27px;color:var(--white)}
.values-lede b{font-weight:500}
.values-lede em{font-style:normal;color:var(--coral)}
.value{left:684px}
.value h4{font-size:17px;font-weight:700;color:var(--white)}
.value p{margin-top:14px;font-size:12.5px;line-height:26.4px;color:var(--white);white-space:nowrap}

/* culture */
.culture{left:0;top:2401px;width:1200px;height:602px;background:var(--pale)}
.culture-title{left:74px;top:2466px}
.culture-copy{left:74px;top:2549px;width:1044px;font-size:12px;line-height:26.4px;color:var(--muted)}
.pillar{width:300px}
.pillar h5{margin-top:12px;font-size:18px;font-weight:400;color:var(--heading)}
.pillar p{margin-top:14px;font-size:12px;line-height:26.4px;color:var(--muted)}
.pillar-div{top:2680px;width:1px;height:230px;background:var(--line)}

/* logo story */
.story-left{left:0;top:3003px;width:625px;height:601px;background:var(--navy)}
.story-note{font-size:12.5px;line-height:26.4px;white-space:nowrap}
.story-note.light{color:var(--white)}
.story-note.dark{color:var(--navy)}
.story-art{left:266px;top:3226px;width:724px;height:190px;background:linear-gradient(90deg,rgba(255,255,255,.14) 0%,rgba(255,255,255,.22) 49.5%,#dfe8f3 50.5%,#c4d5ea 100%)}
</style>
</head>
<body>

<!-- hero -->
<div class="abs hero-photo" role="img" aria-label="Photo looking up at dark glass office towers at dusk with warm lit windows"></div>
<div class="abs brand"><span class="brand-dot"></span>Harlow Vectors</div>
<nav class="abs nav">
  <a style="left:315px">About</a>
  <a style="left:404px">Approach</a>
  <a style="left:516px">Values</a>
  <a style="left:610px">Hiring</a>
  <a style="left:699px">Culture</a>
  <a style="left:796px">What We Want</a>
  <a style="left:937px">Contact</a>
</nav>
<div class="abs login">Log In</div>

<div class="abs band"></div>
<div class="abs band-rule" style="left:75px"></div>
<div class="abs band-rule" style="left:463px"></div>
<div class="abs band-kicker">LOREM IPSUM DOLOR</div>
<div class="abs band-title nowrap">Harlow Vectors is a<br>Lorem ipsum dolor sit<br>amet, consectetur<br>ing elit, sed do eiusmod<br>tempor incididunt ut labore</div>
<div class="abs band-copy nowrap">Lorem ipsum dolor sit amet, consect isicing<br>elit, sed do eiusmod tempor incididunt ut<br>labore et dolore magna aliqua. Ut enim ad<br>minim veniam, quis nostrud exercitation mco<br>laboris nisi ut aliquip</div>
<div class="abs scroll-box">Scroll to discover</div>
<svg class="abs scroll-arrow" width="24" height="34" viewBox="0 0 24 34"><path d="M12 2V30M3 21L12 30L21 21" stroke="#fff" stroke-width="2.5" fill="none"/></svg>

<!-- about -->
<section class="abs about"></section>
<div class="abs about-side"></div>
<div class="abs about-label"><span>ABOUT US</span></div>
<div class="abs about-photo" role="img" aria-label="Photo of modern office buildings against a cloudy sky"></div>
<div class="abs about-card">
  <h3>Lorem Ipsum is<br>simply dummy for</h3>
  <p>Lorem ipsum dolor sit amet, consectetur adipisicing elit, sed do eiusmod tempor incididunt<br>ut labore et dolore magna aliqua. Ut enim ad minim veniam, quis nostrud exercitation ulla-<br>mco laboris nisi ut aliquip ex ea commodo consequat. Duis aute irure dolor in reprehenderit</p>
  <svg class="circle-btn" viewBox="0 0 28 28"><circle cx="14" cy="14" r="13" fill="none" stroke="#0b3d6e" stroke-width="1.3"/><path d="M12 9L17 14L12 19" stroke="#0b3d6e" stroke-width="1.3" fill="none"/></svg>
</div>

<!-- approach -->
<h2 class="abs section-title approach-title">OUR APPROACH</h2>
<div class="abs tabs">
  <div class="tab active" style="left:0"><b>01</b>LOREM IPSUM DOLOR SIT</div>
  <div class="tab-div" style="left:350px"></div>
  <div class="tab" style="left:352px"><b>02</b>LOREM IPSUM DOLOR SIT</div>
  <div class="tab-div" style="left:700px"></div>
  <div class="tab" style="left:702px;width:348px"><b>03</b>LOREM IPSUM DOLOR SIT</div>
</div>
<div class="abs approach-copy">
  <p>
    <span class="jl">Lorem ipsum dolor sit amet, consectetur adipisicing elit, sed do eiusmod tempor incidi-</span>
    <span class="jl">dunt ut labore et dolore magna aliqua. Ut enim ad minim veniam, quis nostrud exercita-</span>
    <span class="jl">tion ullamco laboris nisi ut aliquip ex ea commodo consequat. Duis aute irure dolor in</span>
    <span class="jl">reprehenderit in voluptate velit esse cillum dolore eu fugiat nulla pariatur. Excepteur sint</span>
    <span class="jl">occaecat cupidatat non proident, sunt in culpa qui officia deserunt mollit anim id est</span>
    <span class="jl">laborum. Sed ut perspiciatis unde omnis iste natus error sit voluptatem accusantium do-</span>
  </p>
  <p>
    <span class="jl">Lorem ipsum dolor sit amet, consectetur adipisicing elit, sed do eiusmod tempor incidi-</span>
    <span class="jl">dunt ut labore et dolore magna aliqua. Ut enim ad minim veniam, quis nostrud exercita-</span>
    <span class="jl">tion ullamco laboris nisi ut aliquip ex ea commodo consequat. Duis aute irure dolor in</span>
  </p>
</div>
<div class="abs approach-photo" role="img" aria-label="Photo of a team planning session at a whiteboard covered in sticky notes"></div>
<div class="abs badge">
  <svg width="36" height="36" viewBox="0 0 36 36"><circle cx="18" cy="18" r="15" fill="none" stroke="rgba(255,255,255,.3)" stroke-width="2"/><path d="M18 3A15 15 0 1 1 5 25" fill="none" stroke="#fff" stroke-width="2"/></svg>
  <span>Lorem Ipsum<br>Dolor Sit</span>
</div>

<!-- values -->
<section class="abs values">
  <svg width="1200" height="600" style="position:absolute;left:0;top:0">
    <circle cx="100" cy="170" r="170" fill="#2e4a72"/>
    <circle cx="40" cy="160" r="100" fill="#8f4f5d"/>
    <circle cx="1120" cy="460" r="190" fill="#0f4679"/>
    <circle cx="1150" cy="450" r="110" fill="#114f8f"/>
    <line x1="645" y1="104" x2="645" y2="514" stroke="#8fa7c4" stroke-width="1.5" stroke-dasharray="2 5"/>
    <line x1="508" y1="213" x2="645" y2="213" stroke="#8fa7c4" stroke-width="1.5" stroke-dasharray="2 5"/>
    <line x1="229" y1="278" x2="229" y2="370" stroke="#8fa7c4" stroke-width="1.5" stroke-dasharray="2 5"/>
  </svg>
</section>
<div class="abs values-box">OUR<br>VALUES</div>
<div class="abs values-lede">Lorem Ipsum is<br><b>Simply dummy text</b><br><em>of Printing</em></div>
<div class="abs value" style="top:1925px"><h4>LOREM IPSUM DOLOR SIT</h4><p>Lorem ipsum dolor sit amet, consectetur adipisicing elit, sed do<br>eiusmod tempor incididunt ut labore et dolore magna aliqua. Ut</p></div>
<div class="abs value" style="top:2063px"><h4>LOREM IPSUM DOLOR SIT</h4><p>Lorem ipsum dolor sit amet, consectetur adipisicing elit, sed do<br>eiusmod tempor incididunt ut labore et dolore magna aliqua. Ut</p></div>
<div class="abs value" style="top:2201px"><h4>LOREM IPSUM DOLOR SIT</h4><p>Lorem ipsum dolor sit amet, consectetur adipisicing elit, sed do<br>eiusmod tempor incididunt ut labore et dolore magna aliqua. Ut</p></div>

<!-- culture -->
<section class="abs culture"></section>
<h2 class="abs section-title culture-title">OUR CULTURE</h2>
<p class="abs culture-copy">
  <span class="jl">Lorem ipsum dolor sit amet, consectetur adipisicing elit, sed do eiusmod tempor incididunt ut labore et dolore magna aliqua. Ut enim ad minim veniam, quis nostrud exercitani</span>
  <span class="jl">tion ullamco laboris nisi ut aliquip ex ea commodo consequat. Duis aute irure dolor in reprehenderit in voluptate velit esse cillum dolore eu fugiat nulla pariatur. Excepteur sinta</span>
  <span class="jl">occaecat cupidatat non proident, sunt in culpa qui officia deserunt mollit anim id est laborum. Sed ut perspiciatis unde omnis iste natus error sit voluptatem accusantium dolor</span>
</p>
<div class="abs pillar-div" style="left:413px"></div>
<div class="abs pillar-div" style="left:787px"></div>
<div class="abs pillar" style="left:74px;top:2693px">
  <svg width="34" height="34" viewBox="0 0 34 34"><rect x="3" y="3" width="28" height="28" fill="none" stroke="#0b3d6e" stroke-width="1.3"/><line x1="17" y1="3" x2="17" y2="31" stroke="#0b3d6e" stroke-width="1.3"/><line x1="3" y1="17" x2="31" y2="17" stroke="#0b3d6e" stroke-width="1.3"/></svg>
  <h5>Lorem Ipsum dolor</h5>
  <p><span class="jl">Lorem ipsum dolor sit amet, consectetur adipisic-</span><span class="jl">ing elit, sed do eiusmod tempor incididunt ut</span><span class="jl">labore et dolore magna aliqua. Ut enim ad minim</span><span class="jl">veniam, quis nostrud exercitation ullamco laboris</span><span class="jl">nisi ut aliquip ex ea commodo consequat. Duis</span></p>
</div>
<div class="abs pillar" style="left:449px;top:2693px">
  <svg width="34" height="34" viewBox="0 0 34 34"><circle cx="13" cy="13" r="10" fill="none" stroke="#0b3d6e" stroke-width="1.3"/><line x1="20" y1="20" x2="31" y2="31" stroke="#0b3d6e" stroke-width="2"/><path d="M9 16V13M13 16V9M17 16V11" stroke="#0b3d6e" stroke-width="1.3"/></svg>
  <h5>Lorem Ipsum dolor</h5>
  <p><span class="jl">Lorem ipsum dolor sit amet, consectetur adipisic-</span><span class="jl">ing elit, sed do eiusmod tempor incididunt ut</span><span class="jl">labore et dolore magna aliqua. Ut enim ad minim</span><span class="jl">veniam, quis nostrud exercitation ullamco laboris</span><span class="jl">nisi ut aliquip ex ea commodo consequat. Duis</span></p>
</div>
<div class="abs pillar" style="left:825px;top:2693px">
  <svg width="34" height="34" viewBox="0 0 34 34"><circle cx="17" cy="17" r="13" fill="none" stroke="#0b3d6e" stroke-width="1.3" stroke-dasharray="5 2.5"/><circle cx="17" cy="17" r="6" fill="none" stroke="#0b3d6e" stroke-width="1.3"/></svg>
  <h5>Lorem Ipsum dolor</h5>
  <p><span class="jl">Lorem ipsum dolor sit amet, consectetur adipisic-</span><span class="jl">ing elit, sed do eiusmod tempor incididunt ut</span><span class="jl">labore et dolore magna aliqua. Ut enim ad minim</span><span class="jl">veniam, quis nostrud exercitation ullamco laboris</span><span class="jl">nisi ut aliquip ex ea commodo consequat. Duis</span></p>
</div>

<!-- logo story -->
<div class="abs story-left"></div>
<p class="abs story-note light" style="left:116px;top:3074px">Lorem ipsum dolor sit amet, consectetur adipisicing elit, sed do<br>eiusmod tempor incididunt ut labore et dolore magna aliqua. Ut</p>
<p class="abs story-note dark" style="left:712px;top:3074px">Lorem ipsum dolor sit amet, consectetur adipisicing elit, sed do<br>eiusmod tempor incididunt ut labore et dolore magna aliqua. Ut</p>
<p class="abs story-note light" style="left:116px;top:3479px">Lorem ipsum dolor sit amet, consectetur adipisicing elit, sed do<br>eiusmod tempor incididunt ut labore et dolore magna aliqua. Ut</p>
<p class="abs story-note dark" style="left:712px;top:3479px">Lorem ipsum dolor sit amet, consectetur adipisicing elit, sed do<br>eiusmod tempor incididunt ut labore et dolore magna aliqua. Ut</p>
<div class="abs story-art" role="img" aria-label="Company emblem shown large: a walkway silhouette, solid on the navy side and drawn as a network of joined nodes on the light side"></div>
<svg class="abs" style="left:0;top:3003px" width="1200" height="601">
  <line x1="350" y1="135" x2="350" y2="223" stroke="#fff" stroke-width="1.3"/>
  <line x1="439" y1="413" x2="439" y2="470" stroke="#fff" stroke-width="1.3"/>
  <line x1="913" y1="135" x2="913" y2="223" stroke="#0b3d6e" stroke-width="1.3"/>
  <line x1="807" y1="413" x2="807" y2="470" stroke="#0b3d6e" stroke-width="1.3"/>
</svg>

</body>
</html>
```